New church needs a postcard design to promote free community event for hunters

We are a new church in a rural area of southwest VA- near Halloway Polytech.
We want to reach the hunters, fishermen, and outdoor lovers in our area. We will host a community lunch where we will serve free food, have a bow-hunting seminar, have some encouraging coaching, and give away prizes including a full-sized ATV (picture attached), a new bow- I forget the brand, a trailer, many more door prizes.
I would love to see: dark graphics and backgrounds with reverse font (light text on dark background- neon bright orange or yellow for the text would be great).
We also would like big images including: some type of deer head, a silhouette of a bow-hunter, and the ATV we're giving away would all be great.
Even though we want it to be postcard size, it will be handed out and not mailed, so feel free to use all of both sides.
The basic information:
date: September 19, 2015
time: 11:30 AM
location: Pinecrest Valley High School
Please register for prizes at www.harborlightdq.com/outdoors
At the bottom, I'd like it to say: hosted by Harborlight Church and have our logo (attached).

Thanks!

```html
<!DOCTYPE html>
<html lang="en">
<head>
<meta charset="utf-8">
<title>Community Lunch – Harborlight Church</title>
<link rel="stylesheet" href="https://fonts.googleapis.com/css2?family=Abel&family=Alegreya:wght@500&family=Archivo:wght@800&family=Baloo+2:wght@800&family=Dancing+Script:wght@700&family=Quicksand:wght@700&display=swap">
<style>
  :root {
    --page: #6b6b6b;
    --orange: #e35f22;
    --white: #f7f5f0;
    --photo-top: #3a4049;
    --photo-mid: #3f3c37;
    --photo-bottom: #231c14;
    --buck-light: #9a7a5c;
    --buck-mid: #6e5340;
    --buck-dark: #3b2d22;
  }
  * { margin: 0; padding: 0; box-sizing: border-box; }
  html, body { width: 1200px; height: 900px; overflow: hidden; }
  body {
    background: var(--page);
    position: relative;
    font-family: "Abel", sans-serif;
  }
  .postcard {
    position: absolute;
    left: 50px; top: 25px;
    width: 1100px; height: 845px;
    overflow: hidden;
    box-shadow: 0 6px 22px rgba(0,0,0,.45);
  }
  .backdrop {
    position: absolute; inset: 0;
    background:
      radial-gradient(ellipse 500px 400px at 200px 200px, #2b2e2f 0%, rgba(43,46,47,0) 80%),
      linear-gradient(180deg, var(--photo-top) 0%, var(--photo-mid) 55%, var(--photo-bottom) 100%);
  }
  .buck-photo {
    position: absolute;
    left: 540px; top: 10px;
    width: 560px; height: 835px;
    background:
      radial-gradient(ellipse 110px 150px at 255px 380px, var(--buck-light) 0%, rgba(154,122,92,0) 100%),
      radial-gradient(ellipse 240px 460px at 280px 560px, var(--buck-mid) 0%, rgba(110,83,64,.6) 55%, rgba(110,83,64,0) 100%),
      radial-gradient(ellipse 280px 150px at 280px 140px, rgba(120,104,88,.55) 0%, rgba(120,104,88,0) 100%),
      radial-gradient(ellipse 300px 300px at 380px 760px, var(--buck-dark) 0%, rgba(59,45,34,0) 100%);
  }
  .fade {
    position: absolute; inset: 0;
    background: linear-gradient(180deg, rgba(0,0,0,0) 62%, rgba(25,18,10,.85) 100%);
  }
  .when, .where {
    position: absolute; left: 40px; width: 500px; text-align: center;
  }
  .when { top: 78px; color: var(--white); }
  .when .date { font-size: 46px; line-height: 1; }
  .when .time { font-size: 52px; line-height: 1.1; margin-top: 4px; }
  .accent { color: var(--orange); font-weight: 700; font-family: "Archivo", sans-serif; font-size: .95em; }
  .where {
    top: 222px; color: var(--orange); font-size: 33px; line-height: 1.12;
  }
  .pointer { position: absolute; left: 275px; top: 308px; }
  .prizes {
    position: absolute; left: 25px; top: 340px;
    font-family: "Alegreya", serif; font-weight: 500;
    font-size: 53px; line-height: 1; color: var(--white); letter-spacing: .5px;
    white-space: nowrap;
  }
  .invite-bar {
    position: absolute; left: 0; top: 400px;
    width: 615px; height: 52px;
    background: var(--orange);
    text-align: right; padding-right: 12px;
    font-family: "Archivo", sans-serif; font-weight: 800;
    font-size: 37px; line-height: 52px; color: var(--white);
  }
  .host-name {
    position: absolute; left: 640px; top: 90px;
    font-family: "Abel", sans-serif; font-size: 52px; line-height: .95;
    color: var(--white); text-transform: uppercase; letter-spacing: 1px;
  }
  .host-name span { display: block; font-size: 34px; letter-spacing: 4px; }
  .title { position: absolute; left: 0; width: 1100px; text-align: center; }
  .title-main {
    top: 448px;
    font-family: "Baloo 2", sans-serif; font-weight: 800;
    font-size: 158px; line-height: 1; color: var(--orange);
    -webkit-text-stroke: 3px var(--white); paint-order: stroke fill;
    letter-spacing: 1px;
  }
  .title-sub {
    top: 555px; left: 5px;
    font-family: "Dancing Script", cursive; font-weight: 700;
    font-size: 172px; line-height: 1; color: var(--white);
  }
  .register, .hosted {
    position: absolute; left: 0; width: 1100px; text-align: center; white-space: nowrap;
  }
  .register { top: 733px; font-size: 30px; color: var(--white); }
  .register .link { color: var(--orange); font-weight: 700; font-family: "Archivo", sans-serif; font-size: 25px; }
  .hosted {
    top: 790px; font-family: "Quicksand", sans-serif; font-weight: 700;
    font-size: 23px; letter-spacing: 1.5px; color: var(--orange);
  }
</style>
</head>
<body>
  <main class="postcard">
    <div class="backdrop"></div>
    <div class="buck-photo" role="img" aria-label="Photo of a white-tailed buck with large antlers facing the viewer in a dark forest clearing"></div>
    <div class="fade"></div>

    <div class="when">
      <p class="date">September <span class="accent">19</span>, 2015</p>
      <p class="time"><span class="accent">11:30</span> am</p>
    </div>
    <p class="where">at Pinecrest Valley<br>High School</p>

    <svg class="pointer" width="195" height="30" viewBox="0 0 195 30" aria-hidden="true">
      <path d="M3 26 Q90 -6 186 22" fill="none" stroke="var(--orange)" stroke-width="2.5"/>
      <path d="M175 13 L189 23 L173 27" fill="none" stroke="var(--orange)" stroke-width="2.5"/>
    </svg>

    <p class="prizes">We are giving away prizes!</p>
    <div class="invite-bar">Please come!</div>

    <p class="host-name">Harborlight<span>Church</span></p>

    <h1>
      <span class="title title-main">Community</span>
      <span class="title title-sub">Lunch</span>
    </h1>

    <p class="register">Please register for prizes at <span class="link">www.harborlightdq.com/outdoors</span></p>
    <p class="hosted">Hosted by Harborlight Church (www.harborlightdq.com)</p>
  </main>
</body>
</html>
```